Niche Fitness Rebrand : Q7 Peak Conditioning

We're re-branding our fitness business and need to develop a cleaner, more sophisticated, and sleek website for our clients and potential clients to reference. We're looking to have some photo presence on all pages, with clean, crisp sections for easy reading on the web, and on mobile. We love the BVRdal(.com) website, which represents a very similar target market, and one of the same methods that our business represents. We're looking to take this local studio to a more professional level for future expansion, and need it to be sleek and in line with the growing and competitive marketplace for fitness.
Target Market(s)
70/30 women to men, physically active, upper middle class / professional between the ages of 28-42.
Industry/Entity Type
Fitness
Requirements
Must have
- sleek, professional, high-end design, with easy user navigation.
- About Page - with drop down child pages for management and coaches bios
- Classes Page 'The Methods' - with drop down child pages for different class types
- Location / Schedule Page
- Pricing
- Blog
- Private staff only programming login page
Nice to have
- potential to add an online retail shop -- but not currently necessary.
- Industry websites we like:
- www.bvrdal.example
- www.tarnbrookathletics.example

```html
<!DOCTYPE html>
<html lang="en">
<head>
<meta charset="utf-8">
<title>Q7 Peak Conditioning</title>
<link rel="stylesheet" href="https://fonts.googleapis.com/css2?family=Raleway:wght@300;400;500;600;700&display=swap">
<style>
:root{
  --gold:#b8966a;
  --gold-light:#d4bb95;
  --gold-pale:#e3d2b6;
  --ink:#151515;
  --charcoal:#2b2b2b;
  --grey:#777;
  --cell:#f0f0f0;
  --white:#fff;
}
*{box-sizing:border-box;margin:0;padding:0}
html,body{width:1200px;height:5143px;overflow:hidden}
body{font-family:"Raleway",sans-serif;color:var(--charcoal);background:var(--white)}
section,header,footer{position:relative;width:1200px;overflow:hidden}
.btn{display:inline-block;font-size:16px;font-weight:600;letter-spacing:1px;padding:16px 30px;text-transform:uppercase;white-space:nowrap}
.btn-gold{background:var(--gold);color:var(--white)}
.btn-outline{border:2px solid var(--gold);color:var(--gold)}
.btn-outline-light{border:2px solid var(--gold);color:var(--white)}
.section-title{text-align:center;font-size:42px;font-weight:400;text-transform:uppercase;color:var(--ink);letter-spacing:1px}
.section-title .accent{display:block;color:var(--gold)}
.brand-mark{display:flex;align-items:center;gap:12px;color:var(--white);font-weight:500;font-size:22px;letter-spacing:1px;text-transform:uppercase;white-space:nowrap}
.brand-mark .square{width:40px;height:40px;border:3px solid currentColor}
p.body-text{font-size:14px;line-height:1.75;color:var(--grey)}

/* Hero */
.hero{height:676px;background:#222}
.hero-photo{position:absolute;inset:0;background:linear-gradient(180deg,#3a3a3a 0%,#6b6b6b 40%,#4a4a4a 75%,#1c1c1c 100%)}
.topbar{position:absolute;top:0;left:0;right:0;height:120px;background:rgba(0,0,0,.55);display:flex;align-items:center;padding:0 70px}
.main-nav{margin-left:auto;display:flex;gap:4px;margin-top:26px}
.main-nav a{color:var(--white);font-size:14px;font-weight:500;padding:10px 10px;text-transform:uppercase;text-decoration:none}
.main-nav a.active{border:2px solid var(--gold);color:var(--gold)}
.login{position:absolute;top:18px;right:85px;color:var(--white);font-size:15px;display:flex;align-items:center;gap:8px}
.hero-content{position:absolute;top:270px;width:100%;text-align:center}
.hero-title{font-size:70px;font-weight:300;color:var(--gold-light);letter-spacing:3px;text-transform:uppercase;white-space:nowrap}
.hero-tagline{font-size:30px;color:var(--white);font-weight:500;margin-top:18px}
.hero-actions{margin-top:42px;display:flex;justify-content:center;gap:12px}
.slider-dots{position:absolute;bottom:26px;width:100%;display:flex;justify-content:center;gap:10px}
.slider-dots span{width:12px;height:12px;background:var(--gold-pale)}
.slider-dots span:first-child{background:var(--gold)}

/* Welcome */
.welcome{height:428px;display:flex;padding:70px 90px 0 90px}
.welcome-left{width:430px;text-align:center;padding-top:40px}
.welcome-left .logo-box{width:70px;height:70px;border:4px solid var(--ink);margin:0 auto 30px}
.welcome-left h2{font-size:34px;font-weight:400;color:var(--ink);line-height:1.3;white-space:nowrap}
.welcome-left h2 span{color:var(--gold)}
.welcome-right{margin-left:40px;width:520px}
.welcome-right p{margin-bottom:14px}

/* Classes */
.classes{height:518px}
.gold-photo{position:absolute;inset:0;background:linear-gradient(135deg,#a98a5f 0%,#c9ab7f 45%,#9c7e55 100%)}
.classes .section-title{position:relative;padding-top:58px}
.class-grid{position:relative;display:flex;gap:10px;margin:30px 0 0 75px}
.class-card{width:255px}
.class-card .photo{height:175px;background:linear-gradient(160deg,#cfcfcf,#5d5d5d)}
.class-card .caption{background:var(--ink);color:var(--white);height:92px;padding:14px 14px}
.class-card h3{font-size:15px;font-weight:500;text-transform:uppercase;margin-bottom:8px}
.class-card p{font-size:11px;line-height:1.5;color:#ccc}

/* About */
.about{height:566px;display:flex;padding:65px 0 0 75px}
.about-photo{width:400px;height:420px;background:linear-gradient(150deg,#2c2c2c,#6a6a6a 55%,#2b2b2b)}
.about-text{margin-left:40px;width:600px;padding-top:5px}
.about-text h2{font-size:38px;font-weight:400;color:var(--ink);line-height:1.2;text-transform:uppercase;white-space:nowrap}
.about-text h2 span{color:var(--gold)}
.about-text p{margin:18px 0}

/* Testimonial */
.testimonial{height:426px}
.testimonial-photo{position:absolute;inset:0;background:linear-gradient(90deg,#2d2d2d 0%,#5c5c5c 55%,#9a9a9a 80%,#d8d8d8 100%)}
.testimonial-text{position:absolute;left:75px;top:62px;width:560px;color:var(--white)}
.testimonial-text h2{font-size:42px;font-weight:400;line-height:1.15;text-transform:uppercase}
.testimonial-text h2 span{color:var(--gold)}
.testimonial-text blockquote{margin-top:24px;font-size:13px;line-height:1.75;color:#ddd;position:relative}
.testimonial-text .q{color:var(--gold);font-size:28px;line-height:0}
.author{margin-top:30px;display:flex;gap:12px;align-items:flex-start}
.author .dash{width:30px;height:2px;background:var(--gold);margin-top:8px}
.author strong{display:block;color:var(--gold);font-size:13px;font-weight:600}
.author small{color:#bbb;font-size:12px}

/* Schedule */
.schedule{height:826px;padding-top:66px}
.schedule-table{width:1040px;margin:38px auto 0;border-collapse:separate;border-spacing:2px;font-size:12px}
.schedule-table th{background:var(--gold);color:var(--white);height:42px;font-weight:700;text-transform:uppercase;font-size:13px}
.schedule-table td{background:var(--cell);height:58px;width:140px;text-align:center;color:#666;line-height:1.5}
.schedule-table td.time{background:var(--gold-pale);color:var(--ink);font-weight:600;font-size:14px;width:115px}
.schedule-table td.hl{background:var(--gold-pale)}

/* Blog */
.blog{height:463px}
.blog .section-title{position:relative;padding-top:48px;color:var(--ink)}
.blog-grid{position:relative;display:flex;gap:30px;margin:28px 0 0 80px}
.post{width:330px;height:300px;position:relative;background:linear-gradient(160deg,#d5d5d5,#4d4d4d)}
.post .date{position:absolute;left:0;bottom:0;width:70px;height:92px;background:var(--ink);color:var(--white);text-align:center;padding-top:10px}
.post .date b{display:block;font-size:36px;font-weight:500}
.post .date span{font-size:14px}
.post .title{position:absolute;left:80px;bottom:12px;right:12px;color:var(--white);font-size:20px;line-height:1.25}

/* Pricing */
.pricing{height:717px;padding-top:55px}
.price-grid{display:flex;gap:18px;margin:55px 0 0 80px}
.plan{width:192px;height:475px;background:#f3f3f3;text-align:center}
.plan header{width:auto;background:var(--ink);color:var(--gold);height:92px;display:flex;align-items:center;justify-content:center;font-size:17px;font-weight:500;text-transform:uppercase;line-height:1.3;padding:0 10px}
.plan .item{font-size:14px;color:#555;margin-top:28px;line-height:1.5;padding:0 14px}
.plan .price{font-size:34px;color:var(--gold);margin-top:8px}
.plan.featured{background:var(--gold-light)}
.plan.featured header{color:var(--white)}
.plan.featured .item{margin-top:20px;color:var(--ink)}
.plan.featured .price{color:var(--white);margin-top:2px}

/* Join */
.join{height:172px;background:var(--gold-light);display:flex;align-items:center;padding:0 75px}
.join h2{font-size:38px;font-weight:400;color:var(--ink);text-transform:uppercase;white-space:nowrap}
.join h2 small{font-size:18px;margin-left:6px}
.join .field{margin-left:26px;width:400px;height:56px;background:var(--white);font-size:13px;color:#999;padding:20px 16px}
.join .btn{margin-left:14px;border-color:var(--white);color:var(--white);padding:16px 40px}

/* Footer */
.site-footer{height:351px;background:var(--ink);color:var(--white);display:flex;padding:40px 0 0 125px}
.footer-brand .logo-box{width:150px;height:150px;border:5px solid var(--white);display:flex;align-items:center;justify-content:center;text-align:center;font-size:20px;font-weight:500;letter-spacing:1px;line-height:1.3}
.social{display:flex;gap:10px;margin-top:26px;padding-left:20px}
.social span{width:34px;height:34px;background:var(--gold)}
.footer-col{margin-left:70px}
.footer-col h4{font-size:17px;font-weight:600;text-transform:uppercase;margin-bottom:16px}
.footer-col ul{list-style:none;font-size:13px;line-height:1.85}
.footer-col ul li::before{content:"";display:inline-block;width:6px;height:6px;background:var(--gold);margin-right:10px;vertical-align:middle}
.contact-row{display:flex;gap:12px;font-size:13px;line-height:1.6;margin-bottom:16px;width:260px}
.contact-row svg{flex:none;margin-top:3px}
.map{width:240px;height:180px;background:linear-gradient(135deg,#e6e2d8,#cfd8c9)}
.copyright{position:absolute;bottom:18px;left:0;right:0;text-align:center;font-size:12px;color:#aaa}
.copyright b{color:var(--gold);font-weight:600}
</style>
</head>
<body>

<header class="hero">
  <div class="hero-photo" role="img" aria-label="Black and white photo of a studio class working on reformer machines"></div>
  <div class="topbar">
    <div class="brand-mark"><span class="square"></span>Q7 Peak Conditioning</div>
    <nav class="main-nav">
      <a class="active">Home</a><a>About</a><a>Classes</a><a>Schedule</a><a>Pricing</a><a>Blog</a><a>Shop</a><a>Contact</a>
    </nav>
  </div>
  <div class="login">
    <svg width="14" height="16" viewBox="0 0 14 16"><circle cx="7" cy="4" r="3.5" fill="#fff"/><path d="M0 16c0-5 3-7 7-7s7 2 7 7z" fill="#fff"/></svg>Login
  </div>
  <div class="hero-content">
    <h1 class="hero-title">Q7 Peak Conditioning</h1>
    <p class="hero-tagline">Grow Your Strength</p>
    <div class="hero-actions">
      <span class="btn btn-gold">Know More</span>
      <span class="btn btn-outline-light">Join Us</span>
    </div>
  </div>
  <div class="slider-dots"><span></span><span></span><span></span><span></span></div>
</header>

<section class="welcome">
  <div class="welcome-left">
    <div class="logo-box"></div>
    <h2>WELCOME TO<br><span>Q7 PEAK CONDITIONING</span></h2>
  </div>
  <div class="welcome-right">
    <p class="body-text">Our studio is built around short, focused sessions that challenge every muscle group. Each class is led by a certified coach who adjusts the work to your level, so you leave stronger every week. Small groups keep the attention personal and the energy high from start to finish.</p>
    <p class="body-text">We mix slow, controlled strength work with bursts of cardio to build lasting endurance. Members book online, track their progress and choose from morning, midday and evening times. Whether you are new or experienced, our team will help you set clear goals and reach them safely.</p>
    <span class="btn btn-outline" style="margin-top:8px">Know More</span>
  </div>
</section>

<section class="classes">
  <div class="gold-photo" role="img" aria-label="Gold toned photo of a group training session"></div>
  <h2 class="section-title">Our Classes</h2>
  <div class="class-grid">
    <article class="class-card">
      <div class="photo" role="img" aria-label="Photo of a reformer class"></div>
      <div class="caption"><h3>Peakformer</h3><p>Peak 45 : Signature 45 minute class<br>All Level Class<br>Peak X : Peak Endurance</p></div>
    </article>
    <article class="class-card">
      <div class="photo" role="img" aria-label="Photo of rowing machines in use"></div>
      <div class="caption"><h3>Rowing</h3><p>Row 45 : 45 minute signature row intervals<br>Row X : row + core : strength</p></div>
    </article>
    <article class="class-card">
      <div class="photo" role="img" aria-label="Photo of a core floor class"></div>
      <div class="caption"><h3>Core</h3><p>Core 45 : Signature 45 minute core strength class on the mat<br>Core X : cardio + core endurance</p></div>
    </article>
    <article class="class-card">
      <div class="photo" role="img" aria-label="Photo of a boxing class"></div>
      <div class="caption"><h3>Boxing</h3><p>Box 45 : cardio + footwork is limited<br>Box X : 45 minutes of Boxing</p></div>
    </article>
  </div>
</section>

<section class="about">
  <div class="about-photo" role="img" aria-label="Photo of the studio interior with the brand name on the wall"></div>
  <div class="about-text">
    <h2>About<br><span>Q7 Peak Conditioning</span></h2>
    <p class="body-text">Our studio is built around short, focused sessions that challenge every muscle group. Each class is led by a certified coach who adjusts the work to your level, so you leave stronger every week. Small groups keep the attention personal and the energy high from start to finish.</p>
    <p class="body-text">We mix slow, controlled strength work with bursts of cardio to build lasting endurance. Members book online, track their progress and choose from morning, midday and evening times. Whether you are new or experienced, our team will help you set clear goals and reach them safely.</p>
    <span class="btn btn-outline">View Our Coaches</span>
  </div>
</section>

<section class="testimonial">
  <div class="testimonial-photo" role="img" aria-label="Black and white photo of a client lifting a weight plate"></div>
  <div class="testimonial-text">
    <h2>What Our<br><span>Client Say About Us</span></h2>
    <blockquote><span class="q">&ldquo;</span> Our studio is built around short, focused sessions that challenge every muscle group. Each class is led by a certified coach who adjusts the work to your level, so you leave stronger every week. Small groups keep the attention personal and the energy high from start to finish. <span class="q">&rdquo;</span></blockquote>
    <div class="author"><span class="dash"></span><div><strong>Client Name</strong><small>something.com</small></div></div>
  </div>
</section>

<section class="schedule">
  <h2 class="section-title">Our <span class="accent">Classes Schedule</span></h2>
  <table class="schedule-table">
    <thead><tr><th>Time</th><th>Monday</th><th>Tuesday</th><th>Wednesday</th><th>Thursday</th><th>Friday</th><th>Saturday</th><th>Sunday</th></tr></thead>
    <tbody>
      <tr><td class="time">6:00 AM</td><td class="hl">PEAK :: 45</td><td>PEAK :: 45<br>BOX :: X</td><td class="hl">PEAK :: 45</td><td>PEAK :: 45</td><td class="hl">PEAK :: 45<br>BOX :: X</td><td></td><td></td></tr>
      <tr><td class="time">7:00 AM</td><td></td><td class="hl">PEAK :: 45<br>BOX :: X</td><td>PEAK :: 45</td><td class="hl">PEAK :: 45</td><td>CORE :: 45</td><td></td><td></td></tr>
      <tr><td class="time">8:45 AM</td><td class="hl">PEAK :: 45</td><td></td><td></td><td></td><td></td><td>PEAK :: 45</td><td class="hl">CORE :: 45</td></tr>
      <tr><td class="time">9:30 AM</td><td></td><td></td><td>PEAK :: 45</td><td></td><td></td><td class="hl">CORE :: 45</td><td>CORE :: 45</td></tr>
      <tr><td class="time">9:45 AM</td><td>PEAK :: 45</td><td>PEAK :: 45</td><td class="hl">PEAK :: 45</td><td>PEAK :: 45</td><td class="hl">PEAK :: 45</td><td>PEAK :: 45</td><td class="hl">PEAK :: 45</td></tr>
      <tr><td class="time">12:00 PM</td><td>PEAK :: 45</td><td></td><td></td><td></td><td>PEAK :: 45</td><td></td><td></td></tr>
      <tr><td class="time">5:30 PM</td><td class="hl">CORE :: 45</td><td>CORE :: 45</td><td></td><td>CORE :: 45</td><td></td><td></td><td></td></tr>
      <tr><td class="time">5:45 PM</td><td>PEAK :: 45</td><td class="hl">PEAK :: 45</td><td>PEAK :: 45</td><td class="hl">PEAK :: 45</td><td></td><td></td><td></td></tr>
      <tr><td class="time">6:30 PM</td><td></td><td></td><td class="hl">CORE :: X</td><td></td><td></td><td></td><td></td></tr>
    </tbody>
  </table>
</section>

<section class="blog">
  <div class="gold-photo" role="img" aria-label="Gold toned photo of a studio workout"></div>
  <h2 class="section-title">Latest Blog</h2>
  <div class="blog-grid">
    <article class="post" role="img" aria-label="Black and white photo of a class stretching">
      <div class="date"><b>21</b><span>May</span></div>
      <p class="title">Five simple ways to build your core</p>
    </article>
    <article class="post" role="img" aria-label="Black and white photo of a coach leading a session">
      <div class="date"><b>20</b><span>April</span></div>
      <p class="title">What to eat before an early class</p>
    </article>
    <article class="post" role="img" aria-label="Black and white photo of clients on reformers">
      <div class="date"><b>19</b><span>May</span></div>
      <p class="title">Why rowing belongs in every weekly plan</p>
    </article>
  </div>
</section>

<section class="pricing">
  <h2 class="section-title">Our <span style="color:var(--gold)">Pricing</span></h2>
  <div class="price-grid">
    <div class="plan"><header>Student<br>Pricing</header>
      <p class="item">Unlimited Student 1 Month</p><p class="price">$145</p>
      <p class="item">Student Class Pack</p><p class="price">$155</p></div>
    <div class="plan"><header>1 Month<br>Pricing</header>
      <p class="item">Unlimited Single 1 Month</p><p class="price">$185</p>
      <p class="item">Unlimited Couples 1 Month</p><p class="price">$155</p></div>
    <div class="plan"><header>Contract<br>Pricing</header>
      <p class="item">Unlimited Single Contract</p><p class="price">$175</p>
      <p class="item">Unlimited Couples Contract</p><p class="price">$155</p></div>
    <div class="plan featured"><header>Class<br>Packages</header>
      <p class="item">1 Class</p><p class="price">$25</p>
      <p class="item">4 Classes</p><p class="price">$90</p>
      <p class="item">8 Classes</p><p class="price">$170</p>
      <p class="item">22 Classes</p><p class="price">$395</p></div>
    <div class="plan"><header>New Clients<br>Specials</header>
      <p class="item">New Client 1 Class</p><p class="price">$15</p>
      <p class="item">New Client 15 day's Unlimited</p><p class="price">$55</p></div>
  </div>
</section>

<section class="join">
  <h2>Join Us <small>Q7 Peak Conditioning</small></h2>
  <div class="field">Enter Your Email</div>
  <span class="btn btn-outline">Subscribe</span>
</section>

<footer class="site-footer">
  <div class="footer-brand">
    <div class="logo-box">Q7 PEAK<br>CONDI-<br>TIONING</div>
    <div class="social"><span></span><span></span><span></span></div>
  </div>
  <div class="footer-col">
    <h4>Usefull Links</h4>
    <ul><li>Home</li><li>About</li><li>Classes</li><li>Schedule</li><li>Pricing</li><li>Blog</li><li>Shop</li><li>Contact</li></ul>
  </div>
  <div class="footer-col">
    <h4>Contact Us</h4>
    <div class="contact-row"><svg width="12" height="16" viewBox="0 0 12 16"><path d="M6 0a6 6 0 0 0-6 6c0 4.5 6 10 6 10s6-5.5 6-10a6 6 0 0 0-6-6zm0 8.5A2.5 2.5 0 1 1 6 3.5a2.5 2.5 0 0 1 0 5z" fill="#b8966a"/></svg><span>Q7 PEAK CONDITIONING<br>418 Alder Row<br>Fenwick, VA 22911</span></div>
    <div class="contact-row"><svg width="14" height="14" viewBox="0 0 14 14"><path d="M3 0l2.5 3-1.5 2a8 8 0 0 0 5 5l2-1.5 3 2.5-1.5 3C6 14 0 8 0 1.5z" fill="#b8966a"/></svg><span>+1 555 014 7720</span></div>
    <div class="contact-row"><svg width="16" height="12" viewBox="0 0 16 12"><rect width="16" height="12" fill="#b8966a"/><path d="M0 0l8 6 8-6" stroke="#151515" fill="none"/></svg><span>hello@q7peakconditioning.example</span></div>
  </div>
  <div class="footer-col">
    <h4>Contact Us</h4>
    <div class="map" role="img" aria-label="Street map showing the studio location"></div>
  </div>
  <p class="copyright">&copy; <b>Q7 PEAK CONDITIONING</b> 2017 All rights reserved</p>
</footer>

</body>
</html>
```